Design a CD Cover For Baby Music and Lullabies To Appear on Tune Harbor Shop etc.

Please read this brief before you design. Otherwise you will be wasting your time.

I need a cd cover for music albums which will appear on streaming sites such as Tune Harbor Shop Wavelane, Pluvix etc. for the brand Cozy Cradle Tunes. The thumbnails are quite small so the text needs to be quite large.

I need a design if possible, in which I can simply alter the title of the album and the baby picture so that each album has a different cover but works with the branding.

You can check out the Cozy Cradle Tunes on the Tune Harbor shop.
https://play.wavelane.example/artist/7qk3RtLmWvNx82hYbPdaZe

I made those covers and I really don't like them at all! As you can tell I am not a graphic designer. Ha.

Please help me with a modern, eye catching and cute design that will work across the brand now and in the future. The CCT logo and the name Cozy Cradle Tunes is the only thing that needs to be used somewhere in the design.

Please use the title

Soft Hush Tones For Nap Time Part First

for this first album.
(White noise sounds are hair dryers, vacuum cleaners, fans, wind, rain, the sea, white noise, pink noise, brown noise etc. )

Here is an example of album covers which are coherent. A style like this without the over the top text would be good. But don't copy these!
https://play.wavelane.example/artist/9TfKxcMnEuGh31oAsQbiR5

Target Market(s)

Parents of babies.

Font styles to use
Serif
Sans Serif

Colors

Designer to choose colors to be used in the design.

Requirements
Must have
• Large font so it can been seen in the wavelane thumbnail. A photo of a baby. Please take a look at the wavelane and tune harbor stores. The Cozy Cradle Tunes logo.
• Album Title
• Soft Hush Tones For Nap Time Part First

```html
<!DOCTYPE html>
<html lang="en">
<head>
<meta charset="utf-8">
<title>Soft Hush Tones For Nap Time — Part First</title>
<link rel="stylesheet" href="https://fonts.googleapis.com/css2?family=Jost:wght@300;400&display=swap">
<style>
  :root {
    --stage: #4a4a4a;
    --cover-deep: #1a46a0;
    --cover-mid: #2368b8;
    --cover-light: #2f80c8;
    --photo-blue: #3a92d8;
    --photo-soft: #5aaee6;
    --ink: #f4f6fa;
  }
  * { margin: 0; padding: 0; box-sizing: border-box; }
  html, body {
    width: 1200px;
    height: 960px;
    overflow: hidden;
    background: var(--stage);
  }
  .album-cover {
    position: absolute;
    left: 190px;
    top: 70px;
    width: 820px;
    height: 820px;
    overflow: hidden;
    background:
      radial-gradient(ellipse 70% 60% at 62% 38%, var(--cover-light) 0%, var(--cover-mid) 45%, var(--cover-deep) 100%);
    font-family: "Jost", "Futura", sans-serif;
    color: var(--ink);
  }
  .cover-photo {
    position: absolute;
    left: 70px;
    top: 440px;
    width: 720px;
    height: 270px;
    border-radius: 50% 50% 40% 40% / 60% 60% 40% 40%;
    background:
      radial-gradient(ellipse 60% 70% at 55% 50%, var(--photo-soft) 0%, var(--photo-blue) 55%, rgba(58,146,216,0) 100%);
    opacity: 0.85;
  }
  .album-title { font-weight: 400; }
  .title-line {
    position: absolute;
    left: 0;
    width: 100%;
    text-align: center;
    line-height: 1;
    font-weight: 400;
    white-space: nowrap;
  }
  .title-line--one   { top: 37px;  font-size: 116px; }
  .title-line--two   { top: 146px; font-size: 120px; }
  .title-line--for   { top: 246px; font-size: 102px; }
  .title-line--three { top: 330px; font-size: 122px; }
  .album-part {
    position: absolute;
    left: 0;
    top: 726px;
    width: 100%;
    text-align: center;
    font-size: 46px;
    font-weight: 300;
    letter-spacing: 0.3em;
    line-height: 1;
    padding-left: 0.3em;
  }
  .brand-mark {
    position: absolute;
    left: 0;
    top: 786px;
    width: 100%;
    display: flex;
    justify-content: center;
    align-items: center;
    gap: 10px;
    font-size: 17px;
    font-weight: 400;
    letter-spacing: 0.2em;
    line-height: 1;
    text-transform: uppercase;
  }
  .brand-dot {
    width: 10px;
    height: 10px;
    border-radius: 50%;
    background: var(--ink);
  }
</style>
</head>
<body>
  <main class="album-cover">
    <div class="cover-photo" role="img" aria-label="Photo of a sleeping baby in a blue suit and striped hat lying on a soft blue blanket"></div>
    <h1 class="album-title">
      <span class="title-line title-line--one">SOFT HUSH</span>
      <span class="title-line title-line--two">TONES</span>
      <span class="title-line title-line--for">FOR</span>
      <span class="title-line title-line--three">NAP TIME</span>
    </h1>
    <p class="album-part">PART FIRST</p>
    <p class="brand-mark"><span class="brand-dot"></span><span class="brand-name">Cozy Cradle Tunes</span></p>
  </main>
</body>
</html>
```